North Fern Holdings Business Card

A business card design to accompany the logo design you completed on Artisan Hive. We are open to your proposals. I did add one idea below that might work, but we aren't married to the idea. The company is a real estate services company. Clientele are typically high net worth individuals, executive level employment or owners of their own company, 30-60 years old.

Our 1 (bad?) idea: double sided card; One side landscape with logo and word mark. Other side Portrait with the logo only (oversize watermark maybe?). Somewhere add text of Name (Marcus Pellington), Title (Principal), phone # (949-555-0173) and email address (marcus@northfernhq.com). There would be a second design with my wife's name, number and email in place of mine.

Again totally open to ideas here.

Industry/Entity Type

Real Estate

```html
<!DOCTYPE html>
<html lang="en">
<head>
<meta charset="utf-8">
<title>North Fern Holdings Business Card</title>
<link href="https://fonts.googleapis.com/css2?family=Open+Sans:wght@400;600&display=swap" rel="stylesheet">
<style>
  :root {
    --sage: #659b61;
    --sage-deep: #5a8d57;
    --ink-grey: #6b6b6b;
    --paper: #ffffff;
    --backdrop: #ebe8e3;
  }
  html, body {
    margin: 0;
    width: 1200px;
    height: 1014px;
    overflow: hidden;
    background: var(--backdrop);
    font-family: "Open Sans", Arial, sans-serif;
  }
  .canvas {
    position: relative;
    width: 1200px;
    height: 1014px;
  }
  .card {
    position: absolute;
    box-shadow: 0 6px 18px rgba(0, 0, 0, 0.18);
  }
  .card-front {
    left: 60px;
    top: 90px;
    width: 620px;
    height: 354px;
    background: var(--paper);
  }
  .brand {
    position: absolute;
    left: 44px;
    top: 58px;
    display: flex;
    align-items: center;
    gap: 16px;
  }
  .brand-mark {
    width: 40px;
    height: 40px;
    background: var(--sage);
  }
  .brand-name {
    font-size: 30px;
    font-weight: 400;
    color: var(--sage);
    letter-spacing: 0.5px;
  }
  .edge-tab {
    position: absolute;
    left: 0;
    top: 262px;
    width: 14px;
    height: 64px;
    background: var(--sage);
  }
  .person {
    position: absolute;
    left: 44px;
    top: 258px;
  }
  .person-name {
    margin: 0;
    font-size: 22px;
    font-weight: 600;
    color: var(--sage);
  }
  .person-title {
    margin: 2px 0 0;
    font-size: 18px;
    font-weight: 400;
    color: var(--ink-grey);
  }
  .contact {
    position: absolute;
    left: 390px;
    top: 196px;
    margin: 0;
    padding: 0;
    list-style: none;
    font-size: 15px;
    line-height: 26px;
    color: var(--ink-grey);
  }
  .card-back {
    left: 770px;
    top: 310px;
    width: 354px;
    height: 620px;
    background: var(--sage);
    display: flex;
    align-items: center;
    justify-content: center;
  }
  .back-name {
    font-size: 28px;
    font-weight: 400;
    color: var(--sage-deep);
    text-align: center;
    line-height: 1.3;
  }
</style>
</head>
<body>
<main class="canvas">
  <section class="card card-front" aria-label="Card front">
    <div class="brand">
      <span class="brand-mark"></span>
      <span class="brand-name">North Fern Holdings</span>
    </div>
    <span class="edge-tab"></span>
    <div class="person">
      <p class="person-name">Marcus Pellington</p>
      <p class="person-title">Principal</p>
    </div>
    <ul class="contact">
      <li>phone 949.555.0173</li>
      <li>marcus@northfernhq.com</li>
      <li>www.northfernhq.com</li>
    </ul>
  </section>
  <section class="card card-back" aria-label="Card back">
    <span class="back-name">North Fern Holdings</span>
  </section>
</main>
</body>
</html>
```